Lumora Dwellings

Design a stylish Business card- we would like a businness card design that suits plastic business cards. Our card needs to show that we are tech savy and technology based so the design is crucial.

Target Market(s)

22-40

Industry/Entity Type

Plastic

Requirements
Must have
• attached is our logo. also double sided card would be nice.
my details

Tobias Fenwright
Director
0471596234
www.lumoradwellings.com.au
17 Ashcombe Lane, Eastvale

```html
<!DOCTYPE html>
<html lang="en">
<head>
<meta charset="utf-8">
<title>Lumora Dwellings – Business Card</title>
<link rel="stylesheet" href="https://fonts.googleapis.com/css2?family=Oswald:wght@400;500;700&display=swap">
<style>
  :root {
    --stage: #3a3a3c;
    --card-edge: #141414;
    --card-dark: #262627;
    --card-light: #eeeeee;
    --ink: #1d1d1f;
    --ink-soft: #4a4a4c;
    --accent: #1fa3d4;
  }
  html, body {
    margin: 0;
    width: 1200px;
    height: 900px;
    overflow: hidden;
    background: var(--stage);
  }
  .stage {
    position: relative;
    width: 1200px;
    height: 900px;
  }
  .card {
    position: absolute;
    left: 250px;
    width: 700px;
    height: 380px;
    box-shadow: 0 14px 30px rgba(0,0,0,.45);
    border-radius: 6px;
  }
  .card--front { top: 50px; }
  .card--back { top: 470px; }
  .card svg { display: block; width: 700px; height: 380px; }
  .edge { fill: var(--card-edge); }
  .dark-field { fill: var(--card-dark); }
  .light-field { fill: var(--card-light); }
  .brand-name {
    font-family: 'Oswald', sans-serif;
    font-weight: 700;
    fill: var(--accent);
    letter-spacing: 2px;
  }
  .brand-dot { fill: var(--accent); }
  .web-strip {
    font-family: 'Oswald', sans-serif;
    font-weight: 700;
    font-size: 22px;
    fill: var(--accent);
    letter-spacing: .5px;
  }
  .person-first, .person-last {
    font-family: 'Oswald', sans-serif;
    font-weight: 700;
    font-size: 34px;
  }
  .person-first { fill: var(--ink); }
  .person-last { fill: var(--accent); }
  .person-role {
    font-family: 'Oswald', sans-serif;
    font-weight: 400;
    font-size: 18px;
    fill: var(--ink-soft);
  }
  .contact-line {
    font-family: 'Oswald', sans-serif;
    font-weight: 700;
    font-size: 20px;
    fill: var(--ink);
  }
  .contact-icon { fill: var(--accent); }
  .contact-icon-stroke { fill: none; stroke: var(--accent); stroke-width: 2; }
  .rule { stroke: var(--ink); stroke-width: 1.5; }
</style>
</head>
<body>
<main class="stage">

  <section class="card card--front" aria-label="Card front">
    <svg viewBox="0 0 700 380">
      <rect class="edge" x="0" y="0" width="700" height="380" rx="6"/>
      <rect class="dark-field" x="10" y="10" width="680" height="360" rx="3"/>
      <path class="light-field" d="M10 10 H690 V300 C520 250 280 270 10 360 Z"/>
      <circle class="brand-dot" cx="140" cy="158" r="13"/>
      <text class="brand-name" x="166" y="175" font-size="46">LUMORA DWELLINGS</text>
      <text class="web-strip" x="350" y="352" text-anchor="middle">www.lumoradwellings.com.au</text>
    </svg>
  </section>

  <section class="card card--back" aria-label="Card back">
    <svg viewBox="0 0 700 380">
      <rect class="edge" x="0" y="0" width="700" height="380" rx="6"/>
      <rect class="dark-field" x="10" y="10" width="680" height="360" rx="3"/>
      <path class="light-field" d="M690 10 H300 C170 110 90 240 70 370 H690 Z"/>

      <circle class="brand-dot" cx="34" cy="40" r="7"/>
      <text class="brand-name" x="48" y="47" font-size="19" letter-spacing="1">LUMORA DWELLINGS</text>

      <text x="330" y="110"><tspan class="person-first">Tobias</tspan><tspan class="person-last">Fenwright</tspan></text>
      <text class="person-role" x="620" y="136" text-anchor="end">Director</text>

      <path class="contact-icon" d="M622 172 q4 -4 8 0 l4 5 q2 3 -1 5 l-3 2 q3 7 10 10 l2 -3 q2 -3 5 -1 l5 4 q4 4 0 8 l-3 3 q-10 4 -24 -10 q-14 -14 -10 -24 z"/>
      <text class="contact-line" x="330" y="194">0471596234</text>
      <line class="rule" x1="330" y1="208" x2="655" y2="208"/>

      <circle class="contact-icon-stroke" cx="636" cy="232" r="13"/>
      <ellipse class="contact-icon-stroke" cx="636" cy="232" rx="6" ry="13"/>
      <line class="contact-icon-stroke" x1="623" y1="232" x2="649" y2="232"/>
      <text class="contact-line" x="330" y="240">www.lumoradwellings.com.au</text>
      <line class="rule" x1="330" y1="254" x2="655" y2="254"/>

      <path class="contact-icon" d="M622 280 L636 266 L650 280 H646 V294 H640 V286 H632 V294 H626 V280 Z"/>
      <text class="contact-line" x="330" y="288">17 Ashcombe Lane, Eastvale</text>
    </svg>
  </section>

</main>
</body>
</html>
```